The Festival! Poster for an Annual Dance Showcase

We are looking for a dynamic festival/concert style poster for our annual dance showcase featuring at least one image of our dancers and the main information. The main image should be one of the dancers but there can be a collage of the dancers or smaller images around the poster. I have included some reference images but it can vary from them.

Must have this information;
Date - May 22-26
Location - Mabel Corwin Hale Theatre
Tickets - Vondo.bm

Target Market(s)

Parents and people who love dance

Industry/Entity Type

Dance

Font styles to use
Sans Serif

Colors
E54698
E96AAD
F1A4CE
F9D9EA
FCEFF6

Requirements
Must have
• Logo, Date and Location, Picture of Dancer

```html
<!DOCTYPE html>
<html lang="en">
<head>
<meta charset="utf-8">
<title>Annual Dance Showcase</title>
<link rel="stylesheet" href="https://fonts.googleapis.com/css2?family=Montserrat:wght@300;500;600;700;800&display=swap">
<style>
  :root {
    --bg-deep: #1c0a2e;
    --bg-plum: #3f0747;
    --bg-magenta: #ee00d2;
    --pink: #e80e8f;
    --magenta: #e000c8;
    --cyan: #00d6f2;
    --blue: #1f5fb0;
    --indigo: #3a0c78;
    --white: #ffffff;
    --leotard: #1d5f86;
    --leotard-soft: #6f9db5;
    --skin: #8a5a3e;
    --skirt: #1a1820;
    --skirt-soft: #5a5560;
  }
  * { margin: 0; padding: 0; box-sizing: border-box; }
  html, body { width: 847px; height: 1200px; overflow: hidden; background: var(--bg-deep); }
  .poster {
    position: relative;
    width: 847px;
    height: 1200px;
    overflow: hidden;
    font-family: "Montserrat", sans-serif;
    color: var(--white);
    background: linear-gradient(150deg, #1a2450 0%, var(--bg-deep) 30%, var(--bg-plum) 58%, #8a008a 82%, var(--bg-magenta) 100%);
  }
  .shapes { position: absolute; inset: 0; }
  .hero-photo {
    position: absolute;
    left: -84px; top: -91px;
    width: 666px; height: 666px;
    border-radius: 50%;
    background:
      radial-gradient(ellipse 26% 34% at 42% 62%, var(--leotard) 0%, rgba(29,95,134,0.75) 40%, rgba(111,157,181,0) 100%),
      radial-gradient(ellipse 45% 22% at 55% 44%, rgba(138,90,62,0.55) 0%, rgba(138,90,62,0) 100%),
      radial-gradient(circle at 45% 58%, var(--leotard-soft) 0%, #d6e4ec 42%, #f6f9fb 62%, var(--white) 78%);
  }
  .inset-photo {
    position: absolute;
    left: 387px; top: 300px;
    width: 356px; height: 356px;
    border-radius: 50%;
    border: 3px solid var(--magenta);
    background:
      radial-gradient(ellipse 30% 36% at 52% 72%, var(--skirt) 0%, rgba(26,24,32,0.8) 45%, rgba(26,24,32,0) 100%),
      radial-gradient(ellipse 22% 14% at 56% 44%, rgba(170,200,60,0.55) 0%, rgba(230,90,60,0.3) 55%, rgba(230,90,60,0) 100%),
      radial-gradient(circle at 52% 62%, var(--skirt-soft) 0%, #cfcad1 45%, #f5f3f6 68%, var(--white) 90%);
  }
  .brand {
    position: absolute;
    left: 34px; top: 34px;
    display: flex; align-items: center; gap: 12px;
  }
  .brand-dot { width: 26px; height: 26px; border-radius: 50%; background: var(--pink); }
  .brand-name {
    font-weight: 800;
    color: var(--pink);
    font-size: 30px;
    line-height: 1.02;
    letter-spacing: -0.5px;
  }
  .date-badge {
    position: absolute;
    left: 171px; top: 509px;
    width: 200px; height: 200px;
    border-radius: 50%;
    background: linear-gradient(175deg, var(--cyan) 0%, var(--blue) 50%, var(--indigo) 100%);
    display: flex; flex-direction: column; align-items: center; justify-content: center;
    text-align: center;
  }
  .date-month { font-weight: 600; font-size: 32px; line-height: 1; letter-spacing: 0.5px; color: #eaf7ff; }
  .date-days { font-weight: 800; font-size: 62px; line-height: 1.05; letter-spacing: -1.5px; }
  .invite {
    position: absolute;
    left: 329px; top: 716px;
    width: 438px; height: 60px;
    background: linear-gradient(90deg, var(--magenta) 0%, #8a0aa6 55%, var(--indigo) 100%);
    display: flex; align-items: center; justify-content: center;
    font-weight: 600; font-size: 33px; letter-spacing: 1px;
  }
  .title {
    position: absolute;
    right: 108px; top: 778px;
    text-align: right;
    font-weight: 700;
    font-size: 82px;
    line-height: 90px;
    letter-spacing: 0.5px;
  }
  .venue {
    position: absolute;
    right: 106px; top: 992px;
    font-weight: 700; font-size: 42px; letter-spacing: 0.2px;
  }
  .tickets {
    position: absolute;
    right: 106px; top: 1076px;
    font-weight: 300; font-size: 22px;
  }
  .tickets strong { font-weight: 700; }
</style>
</head>
<body>
<div class="poster">
  <svg class="shapes" width="847" height="1200" viewBox="0 0 847 1200" aria-hidden="true">
    <defs>
      <linearGradient id="grad-magenta" x1="0" y1="0" x2="1" y2="1">
        <stop offset="0" stop-color="#c400d8"/><stop offset="1" stop-color="#ff00c0"/>
      </linearGradient>
      <linearGradient id="grad-cyan" x1="0" y1="0" x2="1" y2="1">
        <stop offset="0" stop-color="#00d6f2"/><stop offset="1" stop-color="#2a4fae"/>
      </linearGradient>
      <linearGradient id="grad-orange" x1="0" y1="0" x2="1" y2="1">
        <stop offset="0" stop-color="#ffb21f"/><stop offset="1" stop-color="#ff6a10"/>
      </linearGradient>
      <linearGradient id="grad-rose" x1="0" y1="0" x2="1" y2="1">
        <stop offset="0" stop-color="#ff6fb4"/><stop offset="1" stop-color="#e8108f"/>
      </linearGradient>
    </defs>
    <circle cx="774" cy="81" r="77" fill="url(#grad-magenta)"/>
    <circle cx="774" cy="81" r="91" fill="none" stroke="#ff6ad6" stroke-width="1.5"/>
    <circle cx="774" cy="81" r="101" fill="none" stroke="#ff6ad6" stroke-width="1.5"/>
    <circle cx="20" cy="992" r="64" fill="url(#grad-cyan)"/>
    <circle cx="20" cy="992" r="74" fill="none" stroke="#ffb8e4" stroke-width="1.5"/>
    <circle cx="20" cy="992" r="84" fill="none" stroke="#ffb8e4" stroke-width="1.5"/>
    <circle cx="20" cy="992" r="92" fill="none" stroke="#ffb8e4" stroke-width="1.5"/>
    <circle cx="276" cy="1202" r="47" fill="none" stroke="url(#grad-cyan)" stroke-width="34"/>
    <polygon points="626,249 683,246 663,295" fill="url(#grad-cyan)"/>
    <polygon points="780,350 834,328 821,385" fill="url(#grad-rose)"/>
    <polygon points="780,609 833,622 792,669" fill="url(#grad-cyan)"/>
    <polygon points="52,616 116,659 54,694" fill="url(#grad-orange)"/>
    <polygon points="222,740 286,712 269,780" fill="url(#grad-orange)"/>
    <polygon points="75,1162 129,1138 128,1200" fill="url(#grad-rose)"/>
    <polygon points="780,1170 834,1181 787,1200" fill="url(#grad-cyan)"/>
  </svg>

  <div class="hero-photo" role="img" aria-label="Photo of a dancer in a blue leotard mid-leap, arm stretched upward"></div>
  <div class="inset-photo" role="img" aria-label="Photo of two dancers in black and floral tops with long sheer skirts posing with arms extended"></div>

  <div class="brand">
    <span class="brand-dot"></span>
    <span class="brand-name">STRIDE HALL<br>DANCE ACADEMY</span>
  </div>

  <div class="date-badge">
    <span class="date-month">MAY</span>
    <span class="date-days">22-26</span>
  </div>

  <div class="invite">COME AND JOIN US</div>

  <h1 class="title">Annual Dance<br>Showcase</h1>

  <p class="venue">Mabel Corwin Hale Theatre</p>
  <p class="tickets">Tickets available at <strong>Vondo.bm</strong></p>
</div>
</body>
</html>
```